Kiswa Design

We need a flyer design for a product that we are a selling, a sacred Islamic cloth called a Kiswah, which is draped around the holy Kaaba in mecca every year.

The details we would like on the flyer are as follows:

Rare Kiswah of the holy Kaaba for sale (fitted in 1977 and 1982 vintage). For sale:

1) whole piece 15 meters x 2.60 meters : £60,000
2) 8 meters x 2.60 meters : £31,200
3) 4 meters x 2.60 meters : £15,600
4) 1 meter : £1500

(insert a high quality picture of holy Kaaba here, then underneath the picture, write the following:) "The Kaaba is covered by an expensive black cloth which is known as 'Kiswah' which is produced and changed every year"

(insert picture of our product here,i.e. use the document named MAIN IMAGE then underneath this picture write the following:) "Silk lampas weave Kiswah, woven silk on a black satin ground with Quranic calligraphy, the zig-zag bands of inscription alternate with the Shahadah and the inscription, 'God, exalted be His Glory!"

insert another picture of kiswah which i provided anywhere you like

(somewhere on flyer write the following) please note a percentage of sales will go towards Sadaqah for our Muslim brothers and sisters in need around the world

(somewhere on flyer write the following) Harwell's international auction house authenticity document also available to prove the Kiswah is genuine.

100% genuine

contact us today! deals this good don't last forever.

email: clothoffer@mailverno.com

Please use the images that I have attached on the flyer accordingly. Also feel free to be as creative as possible I want it to attract a lot of attention but also look professional so you may add some things to improve the look of the flyer.

note: the product being sold is on the pictures I've provided, in particular, i want file 2 "main image" in a large size on the flyer!

thank you! and happy holidays

Target Market(s)

Muslims and Islamic collectors

Industry/Entity Type

House

Requirements
Must have
• the dimensions of the flyer is :
• A5 horizontal or vertical
• (210 x 148 mm)
• must have colors! up to you what colors to choose!

```html
<!DOCTYPE html>
<html lang="en">
<head>
<meta charset="utf-8">
<title>Rare Kiswah of the Holy Kaaba for Sale</title>
<link rel="stylesheet" href="https://fonts.googleapis.com/css2?family=Bebas+Neue&family=Oswald:wght@400;500;700&display=swap">
<style>
  :root {
    --paper: #ffffff;
    --stone: #d9d9d9;
    --stone-light: #ededed;
    --ink: #111111;
    --panel: #3d3d3d;
    --panel-deep: #2b2b2b;
    --white: #ffffff;
    --cloth: #2a2d2c;
    --cloth-light: #4a4e4c;
  }
  * { margin: 0; padding: 0; box-sizing: border-box; }
  html, body { width: 1200px; height: 848px; overflow: hidden; background: var(--paper); }
  .flyer { position: relative; width: 1200px; height: 848px; background: var(--paper); font-family: "Oswald", sans-serif; }

  .sale-area {
    position: absolute; left: 22px; top: 15px; width: 786px; height: 813px;
    background: radial-gradient(ellipse at 40% 45%, var(--stone-light), var(--stone) 80%);
  }

  .title-tab { position: absolute; left: 33px; top: 36px; width: 16px; height: 100px; background: var(--panel); }
  .title-band {
    position: absolute; left: 46px; top: 30px; width: 754px; height: 106px;
    background: var(--ink); color: var(--white);
    font-family: "Bebas Neue", sans-serif; font-size: 46px; line-height: 44px;
    text-align: center; padding-top: 10px; letter-spacing: 0.5px;
  }

  .for-sale-tag {
    position: absolute; left: 118px; top: 155px; width: 42px; height: 162px;
    background: var(--ink); color: var(--white);
    display: flex; align-items: center; justify-content: center;
  }
  .for-sale-tag span {
    transform: rotate(-90deg); white-space: nowrap;
    font-family: "Oswald", sans-serif; font-weight: 700; font-size: 30px; letter-spacing: 1px;
  }
  .price-list {
    position: absolute; left: 180px; top: 156px; list-style: none;
    font-size: 25px; line-height: 41px; color: var(--ink); letter-spacing: 0.6px;
  }

  .photo-circle {
    position: absolute; border-radius: 50%; border: 5px solid var(--ink);
    background: radial-gradient(circle at 45% 40%, var(--cloth-light), var(--cloth) 70%);
  }
  .photo-circle.kaaba { left: 40px; top: 335px; width: 240px; height: 240px; }
  .photo-circle.weave { left: 553px; top: 560px; width: 244px; height: 244px;
    background: radial-gradient(circle at 45% 40%, #6b6f6d, #3a3d3c 70%); }

  .caption {
    position: absolute; background: var(--ink); color: var(--white);
    font-size: 19px; line-height: 25px; letter-spacing: 0.6px; text-align: center;
    display: flex; align-items: center; justify-content: center;
  }
  .caption.kaaba { left: 270px; top: 384px; width: 410px; height: 142px; border-radius: 0 24px 24px 0; padding: 0 22px 0 30px; }
  .caption.weave { left: 150px; top: 594px; width: 430px; height: 176px; border-radius: 24px 0 0 24px; padding: 0 22px; }

  .info-panel {
    position: absolute; left: 808px; top: 15px; width: 367px; height: 813px;
    background: var(--panel); color: var(--white); text-align: center;
  }
  .note { position: absolute; left: 0; width: 100%; font-size: 20px; line-height: 29px; letter-spacing: 0.5px; }
  .note.charity { top: 32px; }
  .note.authenticity { top: 178px; }
  .contact-call { position: absolute; top: 325px; width: 100%; font-size: 29px; font-weight: 500; line-height: 34px; }
  .contact-sub { position: absolute; top: 360px; width: 100%; font-size: 17px; letter-spacing: 0.5px; }
  .contact-rule { position: absolute; left: 8px; top: 394px; width: 348px; height: 1px; background: var(--white); }
  .contact-email { position: absolute; top: 405px; width: 100%; font-size: 17px; letter-spacing: 3.2px; }

  .photo-shadow { position: absolute; left: 0; top: 440px; width: 367px; height: 300px; }
  .product-photo {
    position: absolute; left: 60px; top: 455px; width: 246px; height: 262px;
    border: 5px solid var(--white);
    background: linear-gradient(160deg, #3b3b3b, #1c1c1c 55%, #5a5a5a);
  }
  .genuine-band {
    position: absolute; left: 0; top: 720px; width: 100%; height: 93px; background: var(--ink);
    font-family: "Oswald", sans-serif; font-weight: 700; font-size: 50px; line-height: 93px;
  }
</style>
</head>
<body>
<main class="flyer">
  <section class="sale-area" role="img" aria-label="Pale grey backdrop of embroidered Kiswah calligraphy"></section>

  <div class="title-tab"></div>
  <h1 class="title-band">Rare Kiswah of the Holy Kaaba for sale<br>(Fitted in 1977 and 1982 vintage).</h1>

  <div class="for-sale-tag"><span>FOR SALE</span></div>
  <ol class="price-list">
    <li>1) WHOLE PIECE 15 METERS X 2.60 METERS : £60,000</li>
    <li>2) 8 METERS X 2.60 METERS : £31,200</li>
    <li>3) 4 METERS X 2.60 METERS : £15,600</li>
    <li>4) 1 METER : £1500</li>
  </ol>

  <p class="caption kaaba">"THE KAABA IS COVERED BY AN EXPENSIVE BLACK CLOTH WHICH IS KNOWN AS 'KISWAH' WHICH IS PRODUCED AND CHANGED EVERY YEAR"</p>
  <div class="photo-circle kaaba" role="img" aria-label="Close-up photo of the black Kiswah cloth with woven calligraphy"></div>

  <p class="caption weave">"SILK LAMPAS WEAVE KISWAH, WOVEN SILK ON A BLACK SATIN GROUND WITH QURANIC CALLIGRAPHY, THE ZIG-ZAG BANDS OF INSCRIPTION ALTERNATE WITH THE SHAHADAH AND THE INSCRIPTION, 'GOD, EXALTED BE HIS GLORY!"</p>
  <div class="photo-circle weave" role="img" aria-label="Photo of the silk lampas Kiswah showing zig-zag calligraphy bands"></div>

  <aside class="info-panel">
    <p class="note charity">PLEASE NOTE A PERCENTAGE OF SALES<br>WILL GO TOWARDS SADAQAH FOR<br>OUR MUSLIM BROTHERS AND SISTERS<br>IN NEED AROUND THE WORLD</p>
    <p class="note authenticity">HARWELL'S INTERNATIONAL AUCTION<br>HOUSE AUTHENTICITY DOCUMENT<br>ALSO AVAILABLE TO PROVE<br>THE KISWAH IS GENUINE.</p>
    <p class="contact-call">CONTACT US TODAY!</p>
    <p class="contact-sub">DEALS THIS GOOD DON'T LAST FOREVER.</p>
    <div class="contact-rule"></div>
    <p class="contact-email">EMAIL: CLOTHOFFER@MAILVERNO.COM</p>

    <svg class="photo-shadow" viewBox="0 0 367 300" aria-hidden="true">
      <polygon points="40,20 330,20 300,280 60,280" fill="var(--panel-deep)"/>
    </svg>
    <div class="product-photo" role="img" aria-label="Photo of the folded black Kiswah cloth for sale"></div>

    <p class="genuine-band">100% GENUINE</p>
  </aside>
</main>
</body>
</html>
```